New Business Card Design Project

Want a simple but attention grabbing business card. Back Side having mainly our logo and basic info-the front side a typical business card.

Contact Information for Business Card

Hearth & Tile Interiors
218 NW Larkspur Rd. Suite 207
Ankeny, Iowa 50021

phone- 515.482.7093

website is -htidesigns.com

```html
<!DOCTYPE html>
<html lang="en">
<head>
<meta charset="utf-8">
<title>Hearth &amp; Tile Interiors – Business Card</title>
<link rel="stylesheet" href="https://fonts.googleapis.com/css2?family=Poppins:wght@400;500;600;700&display=swap">
<style>
  :root {
    --stage: #1c1c1e;
    --card: #0b1426;
    --orange: #f0561f;
    --gold-rule: #d98a2b;
    --blue: #2f7fd6;
    --white: #ffffff;
    --muted: #d8dde6;
  }
  * { box-sizing: border-box; margin: 0; padding: 0; }
  html, body {
    width: 1200px; height: 900px; overflow: hidden;
    background: var(--stage);
    font-family: "Poppins", sans-serif;
  }
  .sheet {
    width: 1200px; height: 900px;
    display: flex; flex-direction: column;
    align-items: center; justify-content: center; gap: 34px;
  }
  .card {
    position: relative;
    width: 700px; height: 400px;
    background: var(--card);
    border-radius: 4px;
    box-shadow: 0 14px 30px rgba(0,0,0,.55);
    overflow: hidden;
  }

  /* Front */
  .card-front .brand {
    position: absolute; top: 70px; left: 0; right: 0;
    display: flex; align-items: center; justify-content: center; gap: 12px;
  }
  .brand-mark { width: 14px; height: 14px; background: var(--orange); }
  .brand-name {
    color: var(--orange); font-weight: 600; font-size: 34px;
    letter-spacing: .5px; text-transform: uppercase;
  }
  .rule {
    position: absolute; top: 198px; left: 60px; width: 470px;
    height: 1px; background: var(--gold-rule);
  }
  .contact-list {
    position: absolute; left: 60px; top: 222px;
    list-style: none; display: flex; flex-direction: column; gap: 8px;
  }
  .contact-list li {
    display: flex; align-items: center; gap: 10px;
    color: var(--muted); font-size: 15px; font-weight: 400;
  }
  .contact-list svg { width: 14px; height: 14px; flex: none; }
  .person {
    position: absolute; right: 60px; top: 222px; text-align: right;
  }
  .person-name { color: var(--white); font-weight: 600; font-size: 22px; }
  .person-role { color: var(--orange); font-weight: 500; font-size: 15px; margin-top: 2px; }
  .person-address {
    margin-top: 18px; color: var(--muted); font-size: 14px; line-height: 1.55;
    font-style: normal;
  }

  /* Back */
  .card-back .brand {
    position: absolute; inset: 0;
    display: flex; align-items: center; justify-content: center; gap: 14px;
  }
  .card-back .brand-name { font-size: 44px; font-weight: 700; }
  .card-back .brand-mark { width: 18px; height: 18px; }
</style>
</head>
<body>
<main class="sheet">
  <section class="card card-front" aria-label="Business card front">
    <div class="brand">
      <span class="brand-mark"></span>
      <span class="brand-name">Hearth &amp; Tile Interiors</span>
    </div>
    <div class="rule"></div>
    <ul class="contact-list">
      <li>
        <svg viewBox="0 0 24 24" aria-hidden="true"><path fill="var(--orange)" d="M6.6 10.8a15.1 15.1 0 0 0 6.6 6.6l2.2-2.2c.3-.3.7-.4 1-.2 1.1.4 2.3.6 3.6.6.6 0 1 .4 1 1V20c0 .6-.4 1-1 1A17 17 0 0 1 3 4c0-.6.4-1 1-1h3.5c.6 0 1 .4 1 1 0 1.3.2 2.5.6 3.6.1.3 0 .7-.2 1z"/></svg>
        515.482.7093
      </li>
      <li>
        <svg viewBox="0 0 24 24" aria-hidden="true"><rect x="2" y="5" width="20" height="14" rx="1" fill="var(--orange)"/><path d="M2.5 6l9.5 7 9.5-7" fill="none" stroke="var(--card)" stroke-width="1.6"/></svg>
        dana@htidesigns.com
      </li>
      <li>
        <svg viewBox="0 0 24 24" aria-hidden="true"><circle cx="12" cy="12" r="9.5" fill="none" stroke="var(--orange)" stroke-width="2"/><ellipse cx="12" cy="12" rx="4" ry="9.5" fill="none" stroke="var(--orange)" stroke-width="1.6"/><path d="M2.5 12h19M4 7h16M4 17h16" stroke="var(--orange)" stroke-width="1.4"/></svg>
        htidesigns.com
      </li>
    </ul>
    <div class="person">
      <p class="person-name">Dana Whitfield</p>
      <p class="person-role">CEO/Founder</p>
      <address class="person-address">
        218 NW Larkspur Rd.<br>
        Suite 207, Ankeny<br>
        Iowa 50021
      </address>
    </div>
  </section>

  <section class="card card-back" aria-label="Business card back">
    <div class="brand">
      <span class="brand-mark"></span>
      <span class="brand-name">Hearth &amp; Tile Interiors</span>
    </div>
  </section>
</main>
</body>
</html>
```